qoCover Business Card Design Project

We need a business card design for qoCover. qoCover is an underwriting agency. Underwriting agencies act on behalf of insurers, to underwrite insurance. We will be operating in specialised classes of insurance initially and looking to expand from there. We would like to see designs that incorporate our logo colours as well as a contrasting stand out colour - also we'd like the logo itself to be embossed on the card.

Industry/Entity Type

Insurance

Requirements
Must have
• Logo on front
Nice to have
• Logo solely featured on back of card
Should not have
• Please do not use comic cans font :)

```html
<!DOCTYPE html>
<html lang="en">
<head>
<meta charset="utf-8">
<title>qoCover Business Card</title>
<link href="https://fonts.googleapis.com/css2?family=Arimo:wght@400;700&display=swap" rel="stylesheet">
<style>
  :root {
    --brand-blue: #1456a8;
    --deep-blue: #0b4f93;
    --bright-blue: #2a7cc4;
    --charcoal: #3d3e40;
    --ink: #333333;
    --paper: #ffffff;
    --paper-shade: #eeeeef;
    --edge: #b9b9b9;
  }
  * { box-sizing: border-box; margin: 0; padding: 0; }
  html, body {
    width: 1200px; height: 900px; overflow: hidden;
    background: var(--paper);
    font-family: "Arimo", Arial, sans-serif;
  }
  .canvas { position: relative; width: 1200px; height: 900px; }

  .card {
    position: absolute; top: 284px;
    width: 511px; height: 316px;
    border-radius: 12px; overflow: hidden;
  }

  /* Front */
  .card--front {
    left: 62px;
    background: linear-gradient(180deg, var(--paper-shade) 0%, #fafafa 55%, #f2f2f3 100%);
    border: 1px solid var(--edge);
  }
  .front__band {
    position: absolute; top: 97px; height: 20px; background: var(--brand-blue);
  }
  .front__band--left { left: 0; width: 48px; }
  .front__band--right { left: 228px; right: 0; }
  .front__mark {
    position: absolute; left: 123px; top: 32px;
    width: 50px; height: 50px; border-radius: 50%;
    background: var(--brand-blue);
  }
  .front__name {
    position: absolute; left: 50px; top: 84px;
    font-size: 34px; font-weight: 700; color: var(--brand-blue);
    letter-spacing: -0.5px; line-height: 1;
  }
  .holder {
    position: absolute; right: 285px; top: 160px; text-align: right;
    color: var(--ink); line-height: 1;
  }
  .holder__name { font-size: 16px; font-weight: 700; margin-bottom: 9px; }
  .holder__role { font-size: 15px; font-weight: 700; color: #4a4a4a; }
  .divider {
    position: absolute; left: 233px; top: 151px; width: 1px; height: 71px;
    background: var(--ink);
  }
  .contacts {
    position: absolute; left: 262px; top: 153px; list-style: none;
    font-size: 11.5px; color: var(--ink);
  }
  .contacts li { display: flex; align-items: center; height: 18.5px; }
  .contacts svg { width: 13px; height: 13px; margin-right: 13px; fill: var(--ink); }
  .front__footer, .back__footer {
    position: absolute; left: 0; right: 0; bottom: 0; height: 52px;
    display: flex; align-items: center; justify-content: center;
    color: var(--paper); font-size: 14px; letter-spacing: 3px;
  }
  .front__footer { background: var(--brand-blue); }

  /* Back */
  .card--back {
    left: 635px;
    background: radial-gradient(ellipse at 55% 35%, var(--bright-blue) 0%, var(--deep-blue) 75%);
  }
  .back__footer { background: var(--charcoal); }
  .back__bar {
    position: absolute; top: 167px; height: 34px; background: var(--paper);
  }
  .back__bar--left { left: 0; width: 105px; border-radius: 0 6px 6px 0; }
  .back__bar--right { left: 406px; right: 0; border-radius: 6px 0 0 6px; }
  .back__mark {
    position: absolute; left: 224px; top: 50px;
    width: 70px; height: 70px; border-radius: 50%; background: var(--paper);
  }
  .back__name {
    position: absolute; left: 0; right: 0; top: 151px; text-align: center;
    font-size: 62px; font-weight: 700; color: var(--paper);
    letter-spacing: -1px; line-height: 1;
  }
</style>
</head>
<body>
<main class="canvas">
  <section class="card card--front" aria-label="Card front">
    <div class="front__band front__band--left"></div>
    <div class="front__band front__band--right"></div>
    <div class="front__mark"></div>
    <div class="front__name">qoCover</div>

    <div class="holder">
      <p class="holder__name">Your Name</p>
      <p class="holder__role">Current Postion</p>
    </div>
    <div class="divider"></div>

    <ul class="contacts">
      <li><svg viewBox="0 0 16 16"><path d="M3 1l3 3-2 2c1 2 3 4 5 5l2-2 3 3-2 3C6 15 1 10 1 3z"/></svg>012 345 6789</li>
      <li><svg viewBox="0 0 16 16"><rect x="4" y="1" width="8" height="14" rx="1.5"/></svg>012 345 6789</li>
      <li><svg viewBox="0 0 16 16"><circle cx="8" cy="8" r="6.5"/></svg>yournick@chatline.com</li>
      <li><svg viewBox="0 0 16 16"><rect x="1" y="3" width="14" height="10" rx="1"/></svg>yourmail@qocover.com</li>
    </ul>

    <div class="front__footer">www.yourwebsite.com</div>
  </section>

  <section class="card card--back" aria-label="Card back">
    <div class="back__mark"></div>
    <div class="back__bar back__bar--left"></div>
    <div class="back__bar back__bar--right"></div>
    <div class="back__name">qoCover</div>
    <div class="back__footer">www.yourwebsite.com</div>
  </section>
</main>
</body>
</html>
```